Borvel Stake Pool, redesign of existing website

Borvel is a stake pool that allow its users to stake their Marevo crypto to yearn stable yields. The existing site is at www.borvelstake.org The site is today is a little dull and I want to have suggestions for a redesign that makes the site stand out and that picks up the colors of the logo. I am not looking for a complete redesign, mainly colors and smaller changes to layout. Examples of sites to be inspired by www.quenda.network, https://app.tervalo.finance/

Target Market(s)

Crypto users on Marevo

Number of Pages Required

1 page

```html
<!DOCTYPE html>
<html lang="en">
<head>
<meta charset="UTF-8">
<title>Borvel Stake – Liquid Staking on Marevo</title>
<link href="https://fonts.googleapis.com/css2?family=Poppins:wght@400;500;600&display=swap" rel="stylesheet">
<style>
  :root {
    --navy-deep: #071630;
    --navy: #0c2346;
    --navy-glow: #163a66;
    --teal: #13a0ae;
    --teal-light: #2fc3cf;
    --orange: #f26b1d;
    --white: #ffffff;
    --siren: #e0262a;
  }
  * { box-sizing: border-box; margin: 0; padding: 0; }
  html, body { width: 1200px; height: 821px; overflow: hidden; }
  body {
    font-family: "Poppins", sans-serif;
    color: var(--white);
    background: var(--navy-deep);
  }
  .site {
    position: relative;
    width: 1200px;
    height: 821px;
    overflow: hidden;
  }
  .site-backdrop {
    position: absolute; inset: 0;
    background:
      radial-gradient(circle at 88% 62%, var(--navy-glow) 0%, transparent 38%),
      radial-gradient(circle at 30% 55%, #10305a 0%, transparent 45%),
      linear-gradient(135deg, var(--navy-deep) 0%, var(--navy) 55%, var(--navy-deep) 100%);
  }
  .site-header {
    position: absolute;
    left: 144px; right: 140px; top: 62px;
    display: flex; align-items: center; justify-content: space-between;
  }
  .brand { display: flex; align-items: center; gap: 14px; }
  .brand-dot { width: 28px; height: 28px; border-radius: 50%; background: var(--teal); }
  .brand-name { font-size: 26px; font-weight: 600; color: var(--white); }
  .main-nav { display: flex; align-items: center; }
  .main-nav a {
    color: var(--white); text-decoration: none;
    font-size: 17px; font-weight: 500; letter-spacing: .3px;
    padding: 0 28px;
  }
  .main-nav a.is-active { color: var(--teal-light); }
  .main-nav .nav-sep { width: 1px; height: 26px; background: var(--white); }
  .main-nav .wallet-btn {
    background: var(--teal); border-radius: 14px;
    padding: 4px 26px; margin-left: 2px;
  }

  .intro {
    position: absolute; left: 144px; top: 210px; width: 590px;
  }
  .points-title {
    display: flex; align-items: center; gap: 8px;
    font-size: 19px; font-weight: 600; margin-bottom: 2px;
  }
  .siren { width: 18px; height: 16px; }
  .intro p { font-size: 15.6px; line-height: 22.5px; }
  .headline {
    text-align: center; font-size: 37px; font-weight: 500;
    margin: 30px 0 0;
  }
  .headline-rule {
    width: 200px; height: 3px; background: var(--teal);
    margin: 16px auto 34px;
  }
  .intro .about + .about { margin-top: 16px; }

  .site-footer {
    position: absolute; left: 415px; top: 752px;
    display: flex; gap: 14px; font-size: 16px;
  }
  .site-footer a { color: var(--white); text-decoration: none; }

  .stake-card {
    position: absolute; left: 758px; top: 206px;
    width: 302px; height: 420px;
    background: var(--teal); border-radius: 20px;
    padding: 30px 16px 0;
  }
  .card-tabs { display: flex; justify-content: center; gap: 16px; }
  .card-tabs span {
    background: var(--white); color: #1b2433;
    border-radius: 14px; padding: 3px 10px;
    font-size: 13px; font-weight: 500;
  }
  .card-tabs .is-active { background: var(--orange); color: var(--white); padding: 3px 16px; }
  .apy { text-align: center; font-size: 14px; margin: 34px 0 28px; }
  .amount-field {
    background: var(--white); border-radius: 18px; height: 37px;
    display: flex; justify-content: space-between; align-items: center;
    padding: 0 14px; font-size: 12.5px;
  }
  .amount-field .unit { color: #8a94a3; }
  .amount-field .value { color: #111; font-weight: 500; }
  .field-meta {
    display: flex; justify-content: space-between;
    font-size: 10px; padding: 4px 12px 0;
  }
  .swap-arrow {
    width: 32px; height: 32px; margin: 22px auto 20px;
    border-radius: 50%; background: var(--white);
    display: flex; align-items: center; justify-content: center;
  }
  .connect-btn {
    display: block; width: 170px; margin: 32px auto 0;
    background: var(--orange); color: var(--white);
    text-align: center; border-radius: 14px;
    font-size: 14px; font-weight: 600; padding: 3px 0;
  }
</style>
</head>
<body>
<div class="site">
  <div class="site-backdrop" role="img" aria-label="Dark navy background with a faint glowing network of connected nodes"></div>

  <header class="site-header">
    <div class="brand">
      <span class="brand-dot"></span>
      <span class="brand-name">Borvel Stake</span>
    </div>
    <nav class="main-nav">
      <a href="#" class="is-active">HOME</a>
      <span class="nav-sep"></span>
      <a href="#">VALIDATORS</a>
      <span class="nav-sep"></span>
      <a href="#">DOCS</a>
      <a href="#" class="wallet-btn">SELECT WELLET</a>
    </nav>
  </header>

  <main class="intro">
    <h2 class="points-title">
      <svg class="siren" viewBox="0 0 18 16" aria-hidden="true"><path d="M4 13V8a5 5 0 0 1 10 0v5z" fill="var(--siren)"/><rect x="2" y="13" width="14" height="3" fill="#9aa3ad"/></svg>
      EARN POINTS
      <svg class="siren" viewBox="0 0 18 16" aria-hidden="true"><path d="M4 13V8a5 5 0 0 1 10 0v5z" fill="var(--siren)"/><rect x="2" y="13" width="14" height="3" fill="#9aa3ad"/></svg>
      The Borvel Points Program is live!
    </h2>
    <p>When you stake on Borvel you earn points. Hold it or earn even more points when using your borvel MRV with our defi partners. The amount of points determines what your allocation will be for our future governance token BRV. Leaderboard will be available soon!</p>

    <h1 class="headline">Liquid Staking on Marevo</h1>
    <div class="headline-rule"></div>

    <p class="about">Borvel Stake Pool offers non-custodial staking. Stake your MRV to receive a liquid staking token, borvel MRV, that you can use in Defi on Marevo.</p>
    <p class="about">Let us take care of managing your stake across the best validators on Marevo, and your staking rewards will be automatically compounded each epoch. The value of borvel MRV relative to MRV will increase every epoch.</p>
    <p class="about">It is important for us you feel safe when staking with Borvel! Borvel Stake Pool is based on the Marevo Foundation stake pool program that has been audited 9 times.</p>
  </main>

  <aside class="stake-card">
    <div class="card-tabs">
      <span class="is-active">Stake</span>
      <span>Unstake</span>
      <span>Referral</span>
    </div>
    <p class="apy">Current APY: 8.05% across 60 validators</p>

    <div class="amount-field"><span class="unit">MRV</span><span class="value">0</span></div>
    <div class="field-meta"><span>Balance: 0 MRV</span><span>max half</span></div>

    <div class="swap-arrow">
      <svg width="16" height="16" viewBox="0 0 16 16" aria-hidden="true"><path d="M8 2v11M3 8l5 5 5-5" stroke="var(--orange)" stroke-width="1.6" fill="none" stroke-linecap="round"/></svg>
    </div>

    <div class="amount-field"><span class="unit">borvel MRV</span><span class="value">0</span></div>
    <div class="field-meta"><span>Balance: 0 borvel MRV</span><span>1 borvel MRV ≈ 1.01714 MRV</span></div>

    <a class="connect-btn">CONNECT WELLET</a>
  </aside>

  <footer class="site-footer">
    <a href="#">Defi</a><span>|</span>
    <a href="#">Docs</a><span>|</span>
    <a href="#">Validators</a><span>|</span>
    <a href="#">Huddle</a><span>|</span>
    <a href="#">Chirpwire</a>
  </footer>
</div>
</body>
</html>
```